Motor Vault Website - Part of the Brantley Group

A complimentary website is required for the launch of a 'Motor Vault' - a new service launched by industry renowned BRANTLEY. Motor Vault is an industry-first brand that designs and builds unique subterranean car parks for private residential homes in London and the influential counties within the UK. Please see here the direction of a new BRANTLEY Website - we would like Motor Vault to be complimentary and sit alongside BRANTLEY harmoniously - https://www.brantleyhq.example/ Brantley have some images, but whilst more professional images are in production - we have also attached pixmoor photos- named clearly as pixmoor. **Attached files include JPEG, .eps of logo and Brantley library images and Pixmoor Library Images - two versions of logo dependent on background colour. - Website needs to be sleek, chic and masculine.- Colour Palette - Grey/ Black/ White - Same visiual journey as Brantley website- Required areas within the sit include - About Us / Our Work / Contact Page

Target Market(s)

Luxury
Men

Number of Pages Required

2 page

Font styles to use
Sans Serif

Colors
e8e8e8
757575
1b1b1b
000000
9d9d9d
cbcbcb
f5f5f5

Requirements
Must have
• Complimentary of this site - https://www.brantleyhq.example/
Should not have
• Colour

```html
<!DOCTYPE html>
<html lang="en">
<head>
<meta charset="utf-8">
<title>Motor Vault — Part of the Brantley Group</title>
<link href="https://fonts.googleapis.com/css2?family=Open+Sans:wght@300;400;600;700;800&display=swap" rel="stylesheet">
<style>
  :root {
    --white: #ffffff;
    --paper: #f5f5f5;
    --mist: #e8e8e8;
    --silver: #cbcbcb;
    --ash: #9d9d9d;
    --steel: #757575;
    --coal: #1b1b1b;
    --black: #000000;
    --sans: 'Open Sans', Arial, sans-serif;
  }
  * { box-sizing: border-box; margin: 0; padding: 0; }
  html, body { width: 1200px; height: 2643px; overflow: hidden; background: var(--white); font-family: var(--sans); }
  .page { position: relative; width: 1200px; height: 2643px; overflow: hidden; }
  .abs { position: absolute; }

  /* Hero */
  .hero { left: 0; top: 0; width: 1200px; height: 675px;
    background: radial-gradient(ellipse 22% 26% at 50% 42%, #cfcfcf 0%, #8a8a8a 35%, #3a3a3a 70%, #1a1a1a 100%); }
  .hero-logo { left: 0; width: 1200px; top: 430px; text-align: center; font-weight: 400; font-size: 112px;
    letter-spacing: 2px; color: var(--ash); line-height: 1; white-space: nowrap; }
  .hero-tagline { right: 195px; top: 556px; font-size: 19px; color: var(--ash); letter-spacing: 0.5px; }
  .hero-nav { left: 0; width: 1200px; top: 602px; text-align: center; font-size: 27px; color: var(--white); }
  .hero-nav a { color: inherit; text-decoration: none; margin: 0 4px; }

  /* Section headings */
  .heading { font-size: 40px; font-weight: 400; line-height: 1; display: flex; align-items: center; gap: 42px; white-space: nowrap; }
  .rule { height: 8px; border-radius: 4px; }

  /* About */
  .about { left: 0; top: 675px; width: 1200px; height: 585px; background: var(--white); overflow: hidden; }
  .about .heading { left: 88px; top: 75px; color: var(--coal); }
  .about .rule { left: 62px; top: 121px; width: 366px; background: var(--coal); }
  .wheel-photo { left: -120px; top: 215px; width: 605px; height: 500px; border-radius: 50%;
    background: radial-gradient(circle at 48% 50%, #e8e8e8 0%, #bdbdbd 38%, #8c8c8c 55%, #2a2a2a 62%, #1b1b1b 100%); }
  .about-copy { left: 643px; top: 63px; width: 442px; text-align: right; font-size: 21.5px; line-height: 30px;
    text-transform: uppercase; color: var(--coal); }
  .jump { text-align: center; color: var(--steel); font-size: 27px; white-space: nowrap; }
  .about .jump { left: 810px; top: 500px; width: 150px; }

  /* Work */
  .work { left: 0; top: 1260px; width: 1200px; height: 754px; background: var(--coal); }
  .work-copy { left: 53px; top: 93px; width: 580px; font-size: 22px; line-height: 29px; text-transform: uppercase; color: var(--white); }
  .work .heading { left: 722px; top: 108px; color: var(--white); }
  .work .rule { left: 701px; top: 153px; width: 406px; background: #3a3a3a; }
  .card { top: 241px; width: 327px; height: 356px; background: var(--white); }
  .card-photo { width: 100%; height: 282px; }
  .card-1 { left: 93px; } .card-2 { left: 440px; } .card-3 { left: 788px; }
  .card-1 .card-photo { background: linear-gradient(135deg, #d8d8d8 0%, #6a6a6a 45%, #2b2b2b 100%); }
  .card-2 .card-photo { background: radial-gradient(circle at 62% 18%, #f5f5f5 0%, #8d8d8d 25%, #2e2e2e 65%, #151515 100%); }
  .card-3 .card-photo { background: radial-gradient(ellipse at 55% 30%, #e0e0e0 0%, #777 30%, #2a2a2a 70%, #111 100%); }
  .load-more { left: 460px; top: 631px; width: 266px; height: 24px; border-radius: 5px; background: var(--black);
    color: var(--white); font-size: 11px; line-height: 24px; text-align: center; letter-spacing: 0.3px; }
  .work .jump { left: 103px; top: 663px; font-size: 27px; color: var(--silver); text-align: left; letter-spacing: 0.5px; word-spacing: 6px; }
  .work .jump-icon { left: 158px; top: 710px; }

  /* Group */
  .group-label { left: 0; width: 1200px; top: 2060px; text-align: center; font-size: 24px; color: var(--coal); letter-spacing: 0.5px; }
  .group-logo { left: 123px; top: 2122px; display: flex; align-items: center; gap: 20px;
    font-size: 98px; font-weight: 700; color: var(--coal); line-height: 1; letter-spacing: -1px; white-space: nowrap; }
  .group-logo .mark { width: 72px; height: 72px; background: var(--ash); flex: none; }
  .visit { left: 786px; top: 2141px; width: 317px; height: 70px; border-radius: 6px; background: var(--black);
    color: var(--white); font-size: 40px; text-align: center; line-height: 70px; text-decoration: none; }

  /* Contact */
  .contact-heading { left: 116px; top: 2292px; color: var(--black); }
  .contact-rule { left: 113px; top: 2339px; width: 368px; background: var(--coal); }
  .details { left: 124px; top: 2371px; list-style: none; font-size: 17px; color: var(--coal); }
  .details li { display: flex; align-items: center; height: 32px; white-space: nowrap; }
  .details svg { width: 16px; height: 16px; margin-right: 29px; fill: var(--coal); flex: none; }
  .social { left: 125px; top: 2509px; width: 323px; height: 67px; background: var(--coal);
    display: flex; justify-content: space-around; align-items: center; padding: 0 16px; }
  .social span { width: 36px; height: 36px; background: #4a4a4a; transform: rotate(45deg); }

  .form { left: 601px; top: 2257px; width: 557px; height: 321px; background: var(--black); color: var(--white); }
  .field { font-size: 17px; letter-spacing: 1px; border-bottom: 2px solid var(--white); padding-bottom: 2px; }
  .f-name { left: 30px; top: 36px; width: 231px; }
  .f-mail { left: 296px; top: 36px; width: 231px; }
  .f-subject { left: 30px; top: 119px; width: 497px; border-bottom-color: #5a5a5a; }
  .f-message { left: 30px; top: 156px; width: 497px; height: 103px; border-bottom: 2px solid #5a5a5a; }
  .submit { left: 0; width: 557px; top: 276px; text-align: center; font-size: 17px; }

  .footer { left: 0; top: 2590px; width: 1200px; height: 53px; background: var(--black); color: var(--steel);
    font-size: 11px; line-height: 53px; text-align: center; }
</style>
</head>
<body>
<div class="page">

  <header>
    <div class="abs hero" role="img" aria-label="Black and white photograph of a long concrete underground car park corridor"></div>
    <div class="abs hero-logo">MOTOR VAULT</div>
    <div class="abs hero-tagline">PART OF THE BRANTLEY GROUP</div>
    <nav class="abs hero-nav"><a href="#about">About Us</a> <a href="#work">Our Work</a> <a href="#contact">Contact</a></nav>
  </header>

  <section class="abs about" id="about">
    <h2 class="abs heading">ABOUT US
      <svg width="96" height="24" viewBox="0 0 96 24"><path d="M4 18 L6 11 L26 9 L40 2 L66 2 L78 9 L92 11 L94 18 Z" fill="#1b1b1b"/><circle cx="22" cy="19" r="4.5" fill="#1b1b1b"/><circle cx="76" cy="19" r="4.5" fill="#1b1b1b"/></svg>
    </h2>
    <div class="abs rule"></div>
    <div class="abs wheel-photo" role="img" aria-label="Photograph of a silver five-spoke alloy wheel with tyre"></div>
    <p class="abs about-copy">Lorem ipsum dolor sit amet, consectetur adipiscing elit, sed do eiusmod tempor incididunt ut labore et dolore magna aliqua. Ut enim ad minim veniam, quis nostrud exercitation ullamco laboris nisi ut aliquip ex ea commodo consequat. Duis aute irure dolor in reprehenderit in voluptate velit esse cillum dolore eu fugiat nulla pariatur. Excepteur sint occaecat cupidatat non proident, sunt in culpa qui officia deserunt mollit</p>
    <div class="abs jump">Our Work<br>
      <svg width="28" height="28" viewBox="0 0 28 28"><circle cx="14" cy="14" r="11" fill="none" stroke="#1b1b1b" stroke-width="3"/><path d="M3 13 H25" stroke="#1b1b1b" stroke-width="3"/><circle cx="14" cy="15" r="3.5" fill="#1b1b1b"/></svg>
    </div>
  </section>

  <section class="abs work" id="work">
    <p class="abs work-copy">Lorem ipsum dolor sit amet, consectetur adipiscing elit, sed do eiusmod tempor incididunt ut labore et dolore magna aliqua.</p>
    <h2 class="abs heading">
      <svg width="96" height="24" viewBox="0 0 96 24"><path d="M4 18 L6 11 L26 9 L40 2 L66 2 L78 9 L92 11 L94 18 Z" fill="#ffffff"/><circle cx="22" cy="19" r="4.5" fill="#ffffff"/><circle cx="76" cy="19" r="4.5" fill="#ffffff"/></svg>
      OUR WORK</h2>
    <div class="abs rule"></div>
    <article class="abs card card-1"><div class="card-photo" role="img" aria-label="Black and white photograph of steel girders in an excavated basement"></div></article>
    <article class="abs card card-2"><div class="card-photo" role="img" aria-label="Black and white photograph of light falling into an underground construction site"></div></article>
    <article class="abs card card-3"><div class="card-photo" role="img" aria-label="Black and white photograph of workers beneath a shaft of light on site"></div></article>
    <div class="abs load-more">CLICK TO LOAD MORE WORKS.....</div>
    <div class="abs jump">CONTACT US</div>
    <svg class="abs jump-icon" width="32" height="32" viewBox="0 0 28 28"><circle cx="14" cy="14" r="11" fill="none" stroke="#cbcbcb" stroke-width="2"/><path d="M3 13 H25" stroke="#cbcbcb" stroke-width="2"/><circle cx="14" cy="15" r="3" fill="#cbcbcb"/></svg>
  </section>

  <div class="abs group-label">PROUD PART OF</div>
  <div class="abs group-logo"><span class="mark"></span>Brantley</div>
  <a class="abs visit" href="https://www.brantleyhq.example/">VISIT</a>

  <section id="contact">
    <h2 class="abs heading contact-heading">CONTACT US
      <svg width="96" height="24" viewBox="0 0 96 24" style="margin-left:-30px"><path d="M4 18 L6 11 L26 9 L40 2 L66 2 L78 9 L92 11 L94 18 Z" fill="#1b1b1b"/><circle cx="22" cy="19" r="4.5" fill="#1b1b1b"/><circle cx="76" cy="19" r="4.5" fill="#1b1b1b"/></svg>
    </h2>
    <div class="abs rule contact-rule"></div>
    <ul class="abs details">
      <li><svg viewBox="0 0 16 16"><path d="M8 0 C4.5 0 2 2.6 2 6 C2 10 8 16 8 16 C8 16 14 10 14 6 C14 2.6 11.5 0 8 0 Z M8 8.5 A2.5 2.5 0 1 1 8 3.5 A2.5 2.5 0 1 1 8 8.5 Z"/></svg>48 HARLOW YARD, LONDON, N7 4QT</li>
      <li><svg viewBox="0 0 16 16"><path d="M3 1 L6 1 L7 5 L5 6.5 C6 9 7 10 9.5 11 L11 9 L15 10 L15 13 C15 14 14 15 13 15 C6 15 1 10 1 3 C1 2 2 1 3 1 Z"/></svg>0207 555 0192</li>
      <li><svg viewBox="0 0 16 16"><path d="M1 3 H15 V4 L8 9 L1 4 Z M1 5.5 L8 10.5 L15 5.5 V13 H1 Z"/></svg>MAIL@MOTORVAULT.EXAMPLE</li>
      <li><svg viewBox="0 0 16 16"><circle cx="8" cy="8" r="7" fill="none" stroke="#1b1b1b" stroke-width="1.6"/><ellipse cx="8" cy="8" rx="3" ry="7" fill="none" stroke="#1b1b1b" stroke-width="1.4"/><path d="M1 8 H15" stroke="#1b1b1b" stroke-width="1.4"/></svg>WWW.MOTORVAULT.EXAMPLE</li>
    </ul>
    <div class="abs social"><span></span><span></span><span></span><span></span></div>

    <form class="abs form">
      <div class="abs field f-name">NAME</div>
      <div class="abs field f-mail">E-MAIL</div>
      <div class="abs field f-subject">SUBJECT</div>
      <div class="abs field f-message">MESSAGE</div>
      <div class="abs submit">SUBMIT</div>
    </form>
  </section>

  <footer class="abs footer">COPYRIGHT © BRANTLEY 2018. TERMS AND CONDITIONS | PRIVACY POLICY</footer>
</div>
</body>
</html>
```